Civic Learning Studio PocketDeck

We are looking for a fresh new look for our famous Signal Sense Handset cards. These cards are used as a pedagogical device by teachers and students to help people critically analyze media messages.

Now that we are in the era of Orvo 12, we would like the Signal Sense Handset to look fresh and new. All the content stays the same, but graphic elements, color and overall design can be changed to look contemporary and modern.

Target Market(s)

Teenagers, young adults, secondary and college teachers

Industry/Entity Type

Education

Colors

Designer to choose colors to be used in the design.

Requirements
Must have
• All the content that is on the current card, with icons and text
Nice to have
• Fresh use of color
• More modern phone design like the smartphones people use today
Should not have
• ...too much black

```html
<!DOCTYPE html>
<html lang="en">
<head>
<meta charset="utf-8">
<title>Civic Learning Studio – Signal Sense Handset</title>
<link href="https://fonts.googleapis.com/css2?family=Quicksand:wght@500;600;700&family=Roboto:wght@400;700&display=swap" rel="stylesheet">
<style>
  :root{
    --page:#eeeeee;
    --pink:#ff2a6d;
    --red:#ff3b3b;
    --blue:#1d43d6;
    --violet:#6a2bd8;
    --glow:#fbe9ee;
    --white:#ffffff;
    --card:rgba(255,255,255,.72);
    --ink:#1b1b1b;
    --muted:#5f5f5f;
    --teal:#1fb3c4;
    --green:#5cc44a;
    --yellow:#f6c514;
    --orange:#f36a21;
    --tile:rgba(255,255,255,.82);
    --line:#5a5a5a;
  }
  *{box-sizing:border-box;margin:0;padding:0}
  html,body{width:1200px;height:1199px;overflow:hidden}
  body{background:var(--page);font-family:"Quicksand",sans-serif;position:relative}

  .screen{
    position:absolute;top:212px;width:354px;height:756px;border-radius:42px;overflow:hidden;
    background:
      radial-gradient(ellipse 60% 45% at 58% 62%, var(--glow) 0%, rgba(251,233,238,.6) 40%, rgba(251,233,238,0) 75%),
      radial-gradient(ellipse 70% 40% at 10% 8%, var(--pink) 0%, rgba(255,42,109,0) 80%),
      radial-gradient(ellipse 60% 40% at 95% 10%, var(--blue) 0%, rgba(29,67,214,0) 85%),
      radial-gradient(ellipse 60% 35% at 5% 95%, var(--red) 0%, rgba(255,59,59,0) 80%),
      radial-gradient(ellipse 60% 35% at 100% 92%, var(--violet) 0%, rgba(106,43,216,0) 80%),
      linear-gradient(135deg, var(--pink) 0%, #d63a8c 35%, #f6c6d4 55%, #9a7be0 80%, var(--blue) 100%);
  }
  .screen--questions{left:172px}
  .screen--discuss{left:694px}

  .status{position:absolute;top:14px;left:30px;right:26px;display:flex;justify-content:space-between;align-items:center;color:var(--white);font-family:"Roboto",sans-serif;font-size:13px}
  .status svg{display:block}

  .screen-title{position:absolute;left:0;right:0;text-align:center;color:var(--white);font-weight:600;letter-spacing:1.5px;text-transform:uppercase}
  .screen--questions .screen-title{top:62px;font-size:25px;line-height:32px}
  .screen--discuss .screen-title{top:70px;font-size:25px}

  .question-list{position:absolute;top:146px;left:10px;right:10px;display:flex;flex-direction:column;gap:8px}
  .question{height:83px;border-radius:8px;background:var(--card);padding:10px 10px 0 11px}
  .question-head{display:flex;align-items:center;font-size:10.5px;font-weight:700;color:var(--ink);letter-spacing:.3px}
  .question-num{width:17px;height:17px;border-radius:3px;color:var(--white);font-size:11px;display:flex;align-items:center;justify-content:center;margin-right:8px}
  .question-time{margin-left:auto;font-weight:600}
  .question-text{margin-top:9px;font-size:13px;font-weight:600;line-height:18px;color:var(--ink)}
  .n1,.n5{background:var(--teal)} .n2{background:var(--green)} .n3{background:var(--yellow)} .n4{background:var(--orange)}

  .brand{position:absolute;left:0;right:0;text-align:center;font-family:"Roboto",sans-serif;color:var(--muted)}
  .brand-name{top:606px;font-size:19px;font-weight:700}
  .brand-url{top:630px;font-size:9px;font-weight:700}
  .pager{position:absolute;top:648px;left:0;right:0;display:flex;justify-content:center;gap:6px}
  .pager span{width:5px;height:5px;border-radius:50%;background:rgba(255,255,255,.6)}
  .pager span.on{background:var(--white)}

  .dock{position:absolute;top:662px;left:10px;right:10px;height:86px;border-radius:24px;background:rgba(255,255,255,.8);display:flex;justify-content:space-around;align-items:center;padding:0 12px}
  .dock-tile{width:58px;height:52px}
  .t-teal{background:var(--teal)} .t-green{background:var(--green)} .t-yellow{background:var(--yellow)} .t-orange{background:var(--orange)}

  .app-grid{position:absolute;top:117px;left:12px;right:12px;display:grid;grid-template-columns:repeat(4,1fr);row-gap:20px}
  .app{display:flex;flex-direction:column;align-items:center;text-align:center}
  .app-icon{width:56px;height:56px;border-radius:13px;display:flex;align-items:center;justify-content:center}
  .app-icon.plain{background:var(--tile)}
  .app-icon svg{width:36px;height:36px;fill:none;stroke-width:2.2;stroke-linecap:round;stroke-linejoin:round}
  .app-icon:not(.plain) svg{stroke:var(--white)}
  .app-icon.plain svg{stroke:var(--line)}
  .app-label{margin-top:4px;font-family:"Roboto",sans-serif;font-size:9.5px;line-height:11px;color:var(--white);height:22px}
</style>
</head>
<body>

<section class="screen screen--questions" aria-label="Key questions of media literacy">
  <div class="status"><span>11:53</span>
    <svg width="46" height="11" viewBox="0 0 46 11" fill="#fff"><rect x="0" y="7" width="2.5" height="4"/><rect x="4" y="5" width="2.5" height="6"/><rect x="8" y="3" width="2.5" height="8"/><rect x="12" y="1" width="2.5" height="10"/><path d="M19 4a8 8 0 0 1 11 0l-1.5 1.5a6 6 0 0 0-8 0zM21.5 6.5a4.5 4.5 0 0 1 6 0L24.5 10z"/><rect x="33" y="2" width="11" height="7" rx="2"/></svg>
  </div>
  <h1 class="screen-title">Key Questions of<br>Media Literacy</h1>

  <div class="question-list">
    <article class="question"><div class="question-head"><span class="question-num n1">1</span>QUESTION<span class="question-time">5m ago</span></div><p class="question-text">Who is the author and what<br>is the purpose?</p></article>
    <article class="question"><div class="question-head"><span class="question-num n2">2</span>QUESTION<span class="question-time">4m ago</span></div><p class="question-text">What techniques are used to attract<br>and hold your attention?</p></article>
    <article class="question"><div class="question-head"><span class="question-num n3">3</span>QUESTION<span class="question-time">3m ago</span></div><p class="question-text">What lifestyles, values and points<br>of view are represented?</p></article>
    <article class="question"><div class="question-head"><span class="question-num n4">4</span>QUESTION<span class="question-time">2m ago</span></div><p class="question-text">How might different people<br>interpret the message?</p></article>
    <article class="question"><div class="question-head"><span class="question-num n5">5</span>QUESTION<span class="question-time">1m ago</span></div><p class="question-text">What is omitted from the<br>message?</p></article>
  </div>

  <p class="brand brand-name">Civic Learning Studio</p>
  <p class="brand brand-url">www.civiclearningstudio.org</p>
  <div class="pager"><span></span><span></span><span class="on"></span></div>
  <nav class="dock">
    <div class="dock-tile t-teal" role="img" aria-label="Eye illustration"></div>
    <div class="dock-tile t-green" role="img" aria-label="Joined hands illustration"></div>
    <div class="dock-tile t-yellow" role="img" aria-label="Speaking person illustration"></div>
    <div class="dock-tile t-orange" role="img" aria-label="Tapping finger illustration"></div>
  </nav>
</section>

<section class="screen screen--discuss" aria-label="Time to discuss">
  <div class="status"><span>11:53</span>
    <svg width="46" height="11" viewBox="0 0 46 11" fill="#fff"><rect x="0" y="7" width="2.5" height="4"/><rect x="4" y="5" width="2.5" height="6"/><rect x="8" y="3" width="2.5" height="8"/><rect x="12" y="1" width="2.5" height="10"/><path d="M19 4a8 8 0 0 1 11 0l-1.5 1.5a6 6 0 0 0-8 0zM21.5 6.5a4.5 4.5 0 0 1 6 0L24.5 10z"/><rect x="33" y="2" width="11" height="7" rx="2"/></svg>
  </div>
  <h1 class="screen-title">Time to Discuss</h1>

  <div class="app-grid">
    <div class="app"><div class="app-icon t-teal"><svg viewBox="0 0 36 36"><path d="M6 19l8 8L31 7"/></svg></div><span class="app-label">Reality<br>Check</span></div>
    <div class="app"><div class="app-icon t-green"><svg viewBox="0 0 36 36"><circle cx="21" cy="13" r="7"/><path d="M21 9v8M19 11h3.5a1.5 1.5 0 0 1 0 3h-3M4 26l5-4h6l5 2h6M4 32l6-3h10l10-6"/></svg></div><span class="app-label">Private Gain or<br>Public Good?</span></div>
    <div class="app"><div class="app-icon t-yellow"><svg viewBox="0 0 36 36"><path d="M18 4a13 12 0 1 1-7 22l-6 4 2-7A13 12 0 0 1 18 4z"/><path d="M14 13a4 4 0 1 1 5 4v3M18 24v.5"/></svg></div><span class="app-label">What's<br>Left Out?</span></div>
    <div class="app"><div class="app-icon t-orange"><svg viewBox="0 0 36 36"><path d="M10 6h16l6 8-14 17L4 14zM4 14h28M14 6l-3 8 7 17 7-17-3-8"/></svg></div><span class="app-label">Values<br>Check</span></div>

    <div class="app"><div class="app-icon t-orange"><svg viewBox="0 0 36 36"><circle cx="18" cy="9" r="4"/><path d="M6 20l12 4 12-4v10l-12 4-12-4zM18 24v10"/></svg></div><span class="app-label">Read Between<br>the Lines</span></div>
    <div class="app"><div class="app-icon t-yellow"><svg viewBox="0 0 36 36"><path d="M10 26V16a8 8 0 0 1 16 0v10l3 3H7zM15 31a3 3 0 0 0 6 0M5 12a13 13 0 0 1 3-5M31 12a13 13 0 0 0-3-5"/></svg></div><span class="app-label">Stereotype<br>Alert</span></div>
    <div class="app"><div class="app-icon t-green"><svg viewBox="0 0 36 36"><path d="M5 5h10v4a3 3 0 0 0 6 0V5h10v10h-4a3 3 0 0 0 0 6h4v10H21v-4a3 3 0 0 0-6 0v4H5V21h4a3 3 0 0 0 0-6H5z"/></svg></div><span class="app-label">Solutions<br>too Easy</span></div>
    <div class="app"><div class="app-icon t-teal"><svg viewBox="0 0 36 36"><circle cx="10" cy="18" r="6"/><circle cx="26" cy="18" r="6"/><path d="M10 24h16"/></svg></div><span class="app-label">Record/Save<br>for Later</span></div>

    <div class="app"><div class="app-icon plain"><svg viewBox="0 0 36 36"><path d="M8 8h22v18a3 3 0 0 1-3 3H7a3 3 0 0 1-3-3V13h4zM12 13h14M12 18h14M12 23h10"/></svg></div><span class="app-label">Newspapers</span></div>
    <div class="app"><div class="app-icon plain"><svg viewBox="0 0 36 36"><circle cx="18" cy="20" r="2.5"/><path d="M12 26a8 8 0 1 1 12 0M8 30a13 13 0 1 1 20 0"/></svg></div><span class="app-label">Internet</span></div>
    <div class="app"><div class="app-icon plain"><svg viewBox="0 0 36 36"><rect x="4" y="7" width="28" height="19" rx="1"/><rect x="8" y="11" width="20" height="11"/><path d="M14 30h8M18 26v4"/></svg></div><span class="app-label">TV</span></div>
    <div class="app"><div class="app-icon plain"><svg viewBox="0 0 36 36"><rect x="5" y="15" width="26" height="16"/><path d="M5 15l-1-6 25-4 1 6zM11 8l3 5M18 7l3 5M25 6l3 5"/></svg></div><span class="app-label">Movies</span></div>

    <div class="app"><div class="app-icon plain"><svg viewBox="0 0 36 36"><rect x="4" y="6" width="28" height="22" rx="2"/><path d="M16 32V18a2 2 0 0 1 4 0v6l6 1v7"/></svg></div><span class="app-label">Tablets</span></div>
    <div class="app"><div class="app-icon plain"><svg viewBox="0 0 36 36"><rect x="4" y="11" width="28" height="20" rx="2"/><path d="M8 11l20-6M9 16h18M9 21h12M9 26h12"/><circle cx="27" cy="24" r="2"/></svg></div><span class="app-label">Radio</span></div>
    <div class="app"><div class="app-icon plain"><svg viewBox="0 0 36 36"><rect x="6" y="4" width="24" height="28"/><path d="M6 15h24M18 4v11M6 24h24M14 24v8"/></svg></div><span class="app-label">Comics</span></div>
    <div class="app"><div class="app-icon plain"><svg viewBox="0 0 36 36"><path d="M18 9c-4-3-9-3-14-2v22c5-1 10-1 14 2 4-3 9-3 14-2V7c-5-1-10-1-14 2zM18 9v22M8 13h6M8 18h6M22 13h6M22 18h6"/></svg></div><span class="app-label">Books</span></div>

    <div class="app"><div class="app-icon plain"><svg viewBox="0 0 36 36"><path d="M6 24v-6a12 12 0 0 1 24 0v6"/><rect x="5" y="22" width="6" height="10" rx="2"/><rect x="25" y="22" width="6" height="10" rx="2"/></svg></div><span class="app-label">Music</span></div>
    <div class="app"><div class="app-icon plain"><svg viewBox="0 0 36 36"><circle cx="18" cy="7" r="3"/><circle cx="7" cy="26" r="3"/><circle cx="29" cy="26" r="3"/><path d="M13 8a12 12 0 0 0-8 14M23 8a12 12 0 0 1 8 14M10 29a12 12 0 0 0 16 0"/></svg></div><span class="app-label">Social Media</span></div>
    <div class="app"><div class="app-icon plain"><svg viewBox="0 0 36 36"><path d="M10 10h16a7 7 0 0 1 7 8l-1 7a3 3 0 0 1-6 1l-2-4H12l-2 4a3 3 0 0 1-6-1l-1-7a7 7 0 0 1 7-8zM10 14v6M7 17h6"/><circle cx="24" cy="15" r="1"/><circle cx="28" cy="18" r="1"/></svg></div><span class="app-label">Video Games</span></div>
    <div class="app"><div class="app-icon plain"><svg viewBox="0 0 36 36"><path d="M18 5v12M11 9a11 11 0 1 0 14 0"/></svg></div><span class="app-label">Off</span></div>
  </div>

  <p class="brand brand-name">Civic Learning Studio</p>
  <p class="brand brand-url">www.civiclearningstudio.org</p>
  <div class="pager"><span></span><span class="on"></span><span></span></div>
  <nav class="dock">
    <div class="dock-tile t-teal" role="img" aria-label="Eye illustration"></div>
    <div class="dock-tile t-green" role="img" aria-label="Joined hands illustration"></div>
    <div class="dock-tile t-yellow" role="img" aria-label="Speaking person illustration"></div>
    <div class="dock-tile t-orange" role="img" aria-label="Tapping finger illustration"></div>
  </nav>
</section>

</body>
</html>
```